Website for a company offering full serivce charging solutions for electric cars

The company "vorn-werk" (english: "front-works") offering all-in-one-solutions for charging infrastructure for electric mobility.

There are four products:
1- Wallboxes for single-family homes
2- Solutions for property devloper/-management for property parking space
3- All-in-one-charging solution for municipalities/communities
4- Solutions for tourism/hotels/holiday appartments

The Website structure:
1. Main Page
2.1. Product Page Single Homes
2.2. Product Page Property Management / Parking
2.3. Product Page Municipality
2.4. Product Page Tourism
3. Contact Form / Request for information
4. Imprint / Legal

The Website should be built on Wordpress with a powerful possibility to simply add/modify specific landing pages.

We would like you to implement the website later and also maintain it if possible, but we would be able to do minor modifications by ourselfs (for A/B-Testing)

The website should be clear and simple, easy to understand.
Target group is mainly B2C without deeper knowledge of that topic.

It should suggest, that we will provide a very simple way to get the charging infrastructure done.

We need a contact form, maybe we will use Leadmill later.

Attached you will find a draft of the main page and a landing page (for 2.2) - it is just the content, please ignore the design. We would love to let you create a suitable design.
Also you will find some drafts a bit different for the same story.

I added also a few stock photos, but they don't need to be used! If you have better ideas, you are welcome!

Charging/Electric mobility

Sans Serif

• Based on Wordpress, and the designer should be able to implement it on Wordpress on a later step

```html
<!DOCTYPE html>
<html lang="de">
<head>
<meta charset="utf-8">
<title>vorn-werk – Ladeinfrastruktur</title>
<link href="https://fonts.googleapis.com/css2?family=Oswald:wght@600&family=Exo+2:wght@500&family=Poppins:wght@400;500;600&display=swap" rel="stylesheet">
<style>
:root{
  --ink:#1c1c28;
  --text:#5c5c66;
  --purple:#6b52c4;
  --magenta:#d23698;
  --grad:linear-gradient(90deg,#d8309a,#7a55c8);
  --panel:#f4f4f5;
  --footer:#1b1d2c;
  --footer-line:#34374a;
  --white:#ffffff;
}
*{box-sizing:border-box;margin:0;padding:0}
html,body{width:1200px;height:3520px;overflow:hidden}
body{font-family:"Poppins",sans-serif;color:var(--text);background:var(--white)}
.brand{display:flex;align-items:center;gap:10px;font-family:"Poppins",sans-serif;font-weight:600;font-size:22px;color:var(--ink)}
.brand-dot{width:26px;height:26px;border-radius:50%;background:var(--magenta)}

/* header */
.site-header{height:67px;display:flex;align-items:center;justify-content:space-between;padding:0 162px;border-bottom:1px solid #eee}
.main-nav{display:flex;gap:20px;font-size:13px;font-family:"Exo 2",sans-serif}
.main-nav a{color:#555;text-decoration:none}
.main-nav a.active{color:var(--ink);border-bottom:2px solid var(--magenta);padding-bottom:3px}

/* hero */
.hero{position:relative;height:563px;background:linear-gradient(100deg,#f4f6fb 0%,#e9eef8 45%,#9fb7e8 70%,#3e5fc0 100%)}
.hero-media{position:absolute;right:0;top:0;width:560px;height:100%;background:radial-gradient(circle at 40% 45%,#e0e8fb 0%,#8aa6e6 45%,#2b46a6 100%)}
.hero-copy{position:absolute;left:162px;top:172px}
.hero-title{font-family:"Oswald",sans-serif;font-weight:600;font-size:42px;line-height:54px;color:#111;text-transform:uppercase;letter-spacing:-.3px}
.btn{display:inline-flex;align-items:center;gap:12px;height:40px;padding:0 24px 0 4px;border-radius:20px;font-size:14px;text-decoration:none}
.btn-icon{width:32px;height:32px;border-radius:50%;background:var(--grad)}
.btn-fill{background:var(--grad);color:var(--white);margin-top:34px}
.btn-fill .btn-icon{background:var(--white)}
.btn-outline{border:1.5px solid var(--ink);color:var(--ink)}

/* partner */
.partner{position:relative;height:760px}
.partner-ring{position:absolute;left:180px;top:93px;width:412px;height:412px;border-radius:50%;background:var(--purple)}
.partner-photo{position:absolute;left:198px;top:108px;width:376px;height:450px;background:linear-gradient(160deg,#f3b44f 0%,#c1783a 45%,#3b3a2c 100%);box-shadow:0 10px 25px rgba(0,0,0,.2)}
.partner-copy{position:absolute;left:640px;top:130px;width:400px}
.partner-copy h2{font-family:"Exo 2",sans-serif;font-weight:500;font-size:31px;color:var(--ink)}
.partner-copy h3{font-size:13px;font-weight:600;color:var(--ink);line-height:21px;margin:8px 0 6px}
.partner-copy p{font-size:12.5px;line-height:21.5px;margin-bottom:10px}
.partner-copy .btn{margin-top:4px}
.section-title{position:absolute;top:648px;left:0;width:1200px;text-align:center;font-family:"Exo 2",sans-serif;font-weight:500;font-size:32px;line-height:44px;color:var(--ink)}

/* offers */
.offer{display:flex;height:600px}
.offer-text{width:600px;background:var(--panel);display:flex;flex-direction:column;justify-content:center;padding:0 60px 0 162px}
.offer-text.right{padding-left:68px;padding-right:150px}
.offer-text h3{font-family:"Exo 2",sans-serif;font-weight:500;font-size:21px;color:var(--purple);margin-bottom:14px}
.offer-list{list-style:none;font-size:13px;line-height:20px}
.offer-list li{position:relative;padding-left:19px;margin-bottom:7px}
.offer-list li::before{content:"";position:absolute;left:0;top:6px;width:8px;height:8px;border:1.6px solid var(--magenta);border-radius:50%}
.offer-list ul{list-style:none;margin-top:7px}
.offer-list ul li::before{width:6px;height:6px;border:none;background:var(--magenta);top:7px}
.offer-text .btn{margin-top:24px;align-self:flex-start}
.offer-media{width:600px}
.media-house{background:linear-gradient(180deg,#b7cde6 0%,#e4e4e0 45%,#7f7a72 100%)}
.media-team{background:linear-gradient(160deg,#c9c0b3 0%,#e8e2d8 50%,#8c8273 100%)}
.media-town{background:linear-gradient(180deg,#4d7fd0 0%,#d9c9ae 50%,#857563 100%)}

/* footer */
.site-footer{height:330px;background:var(--footer);color:var(--white);padding:0 162px}
.footer-top{display:flex;align-items:center;justify-content:space-between;height:159px;border-bottom:1px solid var(--footer-line);padding-top:50px}
.footer-top .brand{color:var(--white)}
.contact{display:flex;align-items:center;gap:10px;font-size:13px;line-height:20px}
.contact b{font-weight:600}
.contact-icon{width:40px;height:40px;border-radius:50%;border:1px solid var(--footer-line);display:flex;align-items:center;justify-content:center}
.footer-links{display:flex;justify-content:space-between;height:85px;align-items:center;border-bottom:1px solid var(--footer-line);font-size:13px}
.footer-links a{color:var(--white);text-decoration:none}
.footer-bottom{display:flex;justify-content:space-between;align-items:center;height:84px;font-size:13px}
.social{display:flex;gap:12px}
.social span{width:32px;height:32px;border-radius:50%;border:1px solid #555a70;display:block}
</style>
</head>
<body>
<header class="site-header">
  <div class="brand"><span class="brand-dot"></span>vorn-werk.de</div>
  <nav class="main-nav">
    <a class="active" href="#">Lösungen</a><a href="#">Unternehmen</a><a href="#">Dienstleistungen</a><a href="#">Karriere</a><a href="#">Kontakt</a>
  </nav>
</header>

<section class="hero">
  <div class="hero-media" role="img" aria-label="Ladestecker steckt in einem weißen Elektroauto, blau beleuchtet"></div>
  <div class="hero-copy">
    <h1 class="hero-title">All-in-One-Lösungen für<br>Ladeinfrastruktur für<br>Elektromobilität anzubieten</h1>
    <a class="btn btn-fill" href="#"><span class="btn-icon"></span>Kontaktiere Uns</a>
  </div>
</section>

<section class="partner">
  <div class="partner-ring"></div>
  <div class="partner-photo" role="img" aria-label="Frau mit Smartphone lädt bei Sonnenuntergang ihr Elektroauto"></div>
  <div class="partner-copy">
    <h2>Vorn-werk Ist Ihr Partner</h2>
    <h3>Wenn das Laden nicht nur einfach, sondern die Umsetzung auch aus einer Hand kommen soll</h3>
    <p>Wir bieten Lösungen sowohl für Privatkunden, Geschäftskunden als auch Kommunen an, die schnell, fair und ohne Eigenleistung zu einer smarten Ladelösung für E-Fahrzeuge kommen möchten.</p>
    <p>Von der Beratung, über die Installation, Inbetriebnahme bis zur Abrechnung und Wartung bekommen Sie bei vorn-werk alles aus einer Hand. Auf Wunsch vermieten wir auch die Ladetechnik und übernehmen im gewerblichen Bereich die direkte Abrechnung mit dem Nutzer. Für Kommunen bieten wir den kostenfreien Full-Service an und beteiligen die Gemeinden an der Nutzung der Infrastruktur.</p>
    <a class="btn btn-outline" href="#"><span class="btn-icon"></span>Weiterlesen</a>
  </div>
  <h2 class="section-title">Fragen Sie Uns Nach Der Auf Ihre Individuellen<br>Bedürfnisse Zugeschnittenen Lösung</h2>
</section>

<section class="offer">
  <div class="offer-text">
    <h3>Als Privatkunde</h3>
    <ul class="offer-list">
      <li>Bestandsanalyse mit umfangreicher Beratung über die Möglichkeiten der Umsetzung</li>
      <li>Prüfung und Übernahme der Anmeldung verfügbarer Fördermöglichkeiten</li>
      <li>Auswahl an smarten Wallbox Lösungen, passend für Ihr Fahrzeug und Ihre Bedürfnisse</li>
      <li>Installation inkl. aller notwendigen Materialien und Tätigkeiten (Durchbrüche, Erdarbeiten, etc.)</li>
      <li>Inbetriebnahme und Einweisung in die Ladetechnik</li>
    </ul>
    <a class="btn btn-outline" href="#"><span class="btn-icon"></span>Alle Ansehen</a>
  </div>
  <div class="offer-media media-house" role="img" aria-label="Moderne weiße Einfamilienhäuser unter blauem Himmel"></div>
</section>

<section class="offer">
  <div class="offer-media media-team" role="img" aria-label="Team arbeitet an einem großen Tisch mit Laptops, von oben gesehen"></div>
  <div class="offer-text right">
    <h3>Als Geschäftskunde</h3>
    <ul class="offer-list">
      <li>Durchführung einer individuellen Bedarfsanalyse inkl. Ermittlung der Anforderungen für:
        <ul>
          <li>Haus- und Immobilienverwaltungen</li>
          <li>Dienstleistungs- und Handelsunternehmen</li>
          <li>Hotel und Beherbergungsbetriebe</li>
          <li>Parkraum- und Parkhausbetreiber</li>
          <li>Tourismus, Sport- und Freizeiteinrichtungen</li>
        </ul>
      </li>
      <li>Planung und Projektierung des Installationsaufwands inkl. Materialverbrauch</li>
      <li>Leasing oder Kauf der Hardware</li>
    </ul>
    <a class="btn btn-outline" href="#"><span class="btn-icon"></span>Alle Ansehen</a>
  </div>
</section>

<section class="offer">
  <div class="offer-text">
    <h3>Als Kommune</h3>
    <ul class="offer-list">
      <li>Konzeptionierung möglicher Ladeinfrastrukturen innerhalb Ihrer Gemeinde</li>
      <li>Planung und Projektsteuerung inkl. sämtlicher behördlicher Genehmigungsverfahren und Beantragung von Fördermitteln</li>
      <li>Fachgerechte Installation und Inbetriebnahme</li>
      <li>Regelmäßige Wartung gemäß Vorschrift</li>
      <li>Reparatur und Kundenservice</li>
      <li>Direkte Abrechnung mit dem Nutzer</li>
    </ul>
    <a class="btn btn-outline" href="#"><span class="btn-icon"></span>Alle Ansehen</a>
  </div>
  <div class="offer-media media-town" role="img" aria-label="Historisches Thermalbad-Gebäude mit Türmen vor blauem Himmel"></div>
</section>

<footer class="site-footer">
  <div class="footer-top">
    <div class="brand"><span class="brand-dot"></span>vorn-werk.de</div>
    <div class="contact">
      <span class="contact-icon"><svg width="14" height="18" viewBox="0 0 14 18"><path d="M7 1a6 6 0 0 0-6 6c0 4.5 6 10 6 10s6-5.5 6-10a6 6 0 0 0-6-6z" fill="none" stroke="#d23698" stroke-width="1.6"/><circle cx="7" cy="7" r="2" fill="#d23698"/></svg></span>
      <span>123, Gebäudename, Straße<br>Stadt, Bundesland XY 123456</span>
    </div>
    <div class="contact">
      <span class="contact-icon"><svg width="16" height="16" viewBox="0 0 16 16"><path d="M3 1l3 3-2 2a10 10 0 0 0 6 6l2-2 3 3-2 2C7 15 1 9 1 3z" fill="none" stroke="#d23698" stroke-width="1.5"/></svg></span>
      <span><b>Telefon</b><br>123-456-7890</span>
    </div>
    <div class="contact">
      <span class="contact-icon"><svg width="16" height="12" viewBox="0 0 16 12"><rect x="0.5" y="0.5" width="15" height="11" rx="1.5" fill="#d23698"/><path d="M1 1l7 6 7-6" fill="none" stroke="#1b1d2c" stroke-width="1.3"/></svg></span>
      <span><b>Email</b><br>info@vorn-werk.com</span>
    </div>
  </div>
  <nav class="footer-links">
    <a href="#"><b>AGB</b></a><a href="#">Datenschutzerklärung</a><a href="#">FAQs</a><a href="#">Karriere</a><a href="#">Impressum</a><a href="#">Kontakt</a>
  </nav>
  <div class="footer-bottom">
    <span>Copyright © 2022 Vorn-werk GmbH. All Rights Reserved.</span>
    <div class="social"><span></span><span></span><span></span></div>
  </div>
</footer>
</body>
</html>
```